Professional Kiosk Poster for Logistics Trade Show

We need a graphic for our kiosk at a tradeshow. 38 13/16”W x 56 1/8”H.<br/><br/>We are a platform to match eCommerce parcel shipments with the most cost effective carrier for each package. We help eCommerce companies reduce their shipping costs and reduce the carbon impact of their shipments.<br/><br/>We would like to see something professional looking that incorporates our logo and the tag-line "Financially & Environmentally Sustainable eCommerce Shipping".<br/><br/>We would also like a call to action on the poster asking customers to contact "info@Velbrix.com"<br/><br/>Have included all logos we originally received. Can't open them on my own, as they're in formats I don't have software for. We use the blue and grey logo that can be seen on our website: www.velbrix.com<br/><br/>Design in line with our website would be appropriate. Have included potenaitl background images. Open to other options

Target Market(s)

Target is a business oriented trade show

Industry/Entity Type

Logistics

Colors

Designer to choose colors to be used in the design.

Requirements
Must have
• Must have company logo and contact information
Nice to have
• Nice to have our tagline. Nice to use a background image, although open to other options.
Should not have
• Should not be overly busy

```html
<!DOCTYPE html>
<html lang="en">
<head>
<meta charset="utf-8">
<title>Velbrix – Sustainable eCommerce Shipping</title>
<link rel="stylesheet" href="https://fonts.googleapis.com/css2?family=Poppins:wght@300;400;600;800&display=swap">
<style>
  :root {
    --brand-blue: #1fa3de;
    --white: #ffffff;
    --band-navy: #262b3b;
    --sky-top: #13264a;
    --sky-mid: #2c4a78;
    --dusk: #6b7f9e;
    --city-dark: #1d2430;
    --road-dark: #2a2c33;
    --trail-red: #7a3228;
  }
  * { margin: 0; padding: 0; box-sizing: border-box; }
  html, body { width: 830px; height: 1200px; overflow: hidden; background: var(--band-navy); }
  .poster {
    position: relative;
    width: 830px;
    height: 1200px;
    overflow: hidden;
    font-family: "Poppins", Arial, sans-serif;
    background: var(--band-navy);
  }
  .hero-photo {
    position: absolute;
    left: 0; top: 0;
    width: 830px; height: 1003px;
    background:
      radial-gradient(ellipse 60% 30% at 50% 78%, rgba(160,60,40,0.35), transparent 70%),
      linear-gradient(180deg,
        var(--sky-top) 0%,
        var(--sky-mid) 18%,
        var(--dusk) 30%,
        var(--city-dark) 40%,
        #232a33 52%,
        var(--road-dark) 70%,
        var(--trail-red) 88%,
        #3a2a2c 100%);
  }
  .bottom-band {
    position: absolute;
    left: 0; top: 1003px;
    width: 830px; height: 197px;
    background: var(--band-navy);
  }
  .tagline {
    position: absolute;
    left: 0; top: 128px;
    width: 830px;
    text-align: center;
    font-weight: 800;
    text-transform: uppercase;
    color: var(--brand-blue);
    text-shadow: 0 4px 8px rgba(0,0,0,0.45);
  }
  .tagline .line { display: block; font-size: 62px; line-height: 71px; letter-spacing: 1px; }
  .tagline .line-strong { color: var(--white); font-size: 78px; line-height: 88px; }
  .contact-cta {
    position: absolute;
    left: 0; top: 664px;
    width: 830px;
    text-align: center;
  }
  .mail-icon { display: block; margin: 0 auto; width: 86px; height: 86px; }
  .cta-email {
    margin-top: 34px;
    font-weight: 400;
    font-size: 51px;
    letter-spacing: 1px;
    color: var(--white);
  }
  .brand-mark {
    position: absolute;
    left: 0; top: 925px;
    width: 830px;
    display: flex;
    justify-content: center;
    align-items: center;
    gap: 18px;
  }
  .brand-dot {
    width: 110px; height: 110px;
    border-radius: 50%;
    background: var(--brand-blue);
  }
  .brand-name {
    font-weight: 600;
    font-size: 118px;
    line-height: 1;
    color: var(--brand-blue);
    letter-spacing: -2px;
  }
  .contact-details {
    position: absolute;
    left: 0; top: 1108px;
    width: 830px;
    text-align: center;
    color: var(--white);
    font-weight: 400;
    font-size: 28px;
    line-height: 37px;
    letter-spacing: 1.5px;
  }
  .contact-details b { font-weight: 600; }
  .contact-details .sep { margin: 0 14px; }
</style>
</head>
<body>
<main class="poster">
  <div class="hero-photo" role="img" aria-label="Photo of a city skyline at dusk above a highway with red and white light trails from traffic"></div>
  <div class="bottom-band"></div>

  <h1 class="tagline">
    <span class="line">Financially &amp;</span>
    <span class="line">Environmentally</span>
    <span class="line">Sustainable</span>
    <span class="line line-strong">eCommerce</span>
    <span class="line">Shipping</span>
  </h1>

  <section class="contact-cta">
    <svg class="mail-icon" viewBox="0 0 86 86" aria-hidden="true">
      <circle cx="43" cy="43" r="40" fill="var(--brand-blue)" stroke="var(--white)" stroke-width="6"/>
      <rect x="24" y="30" width="38" height="27" rx="4" fill="var(--white)"/>
      <path d="M26 33 L43 46 L60 33" fill="none" stroke="var(--brand-blue)" stroke-width="3" stroke-linejoin="round"/>
    </svg>
    <p class="cta-email">info@Velbrix.com</p>
  </section>

  <div class="brand-mark">
    <span class="brand-dot"></span>
    <span class="brand-name">Velbrix</span>
  </div>

  <p class="contact-details">
    <b>P:</b> 1200 555 0148<span class="sep">|</span><b>E:</b> info@Velbrix.com<br>
    <b>W:</b> www.Velbrix.com
  </p>
</main>
</body>
</html>
```